Natural Cosmetics need a Packaging Design

We need a PACKAGING design for labels on hand/body wash bottles and soap paper boxes.
We target at high end markets.
We expect a contemporary and trendy design.
We don't need a separate logo. The brand name "Ma Vitrine" acts as the logo.
We want a modern and classic font for "Ma Vitrine".
Please see attached pictures for packaging samples.

Industry/Entity Type

Cosmetics

Requirements
Should not have
• a separate logo from the brand name

```html
<!DOCTYPE html>
<html lang="en">
<head>
<meta charset="utf-8">
<title>Ma Vitrine — Bath Labels</title>
<link rel="stylesheet" href="https://fonts.googleapis.com/css2?family=Montserrat:wght@400&family=Tinos:wght@400&display=swap">
<style>
  :root {
    --bg: #f2f2f0;
    --label: #ffffff;
    --ink: #1e1e1e;
    --teal: #2d9cb7;
    --teal-band: #2a95ae;
    --plum: #9e4a86;
    --plum-band: #a04d87;
    --bronze: #7d6136;
    --gold: #c9a24a;
    --line-teal: #bcdde6;
    --line-plum: #ead3e2;
  }
  * { box-sizing: border-box; margin: 0; padding: 0; }
  html, body { width: 1001px; height: 1200px; overflow: hidden; }
  body { background: var(--bg); position: relative; font-family: "Tinos", "Times New Roman", serif; color: var(--ink); }

  .label {
    position: absolute;
    background: var(--label);
    box-shadow: 0 2px 10px rgba(0,0,0,0.08);
    text-align: center;
  }
  .label--wash { left: 119px; top: 285px; width: 294px; height: 815px; }
  .label--gel  { left: 563px; top: 678px; width: 293px; height: 391px; }

  .brand {
    position: absolute; left: 0; right: 0;
    font-family: "Tinos", "Times New Roman", serif;
    font-weight: 400; color: var(--ink);
  }
  .label--wash .brand { top: 128px; font-size: 36px; }
  .label--gel .brand  { top: 50px;  font-size: 30px; }

  .product {
    position: absolute; left: 0; right: 0;
    font-family: "Montserrat", Arial, sans-serif; font-weight: 400;
    text-transform: uppercase; line-height: 1.12;
  }
  .label--wash .product { top: 240px; font-size: 36px; color: var(--teal); letter-spacing: 0.5px; }
  .label--gel .product  { top: 104px; font-size: 27px; color: var(--plum); }

  .claim { position: absolute; left: 0; right: 0; line-height: 1.15; }
  .label--wash .claim { top: 323px; font-size: 22px; color: var(--bronze); }
  .label--gel .claim  { top: 138px; font-size: 14px; color: var(--plum); }

  .illustration { position: absolute; left: 20px; right: 20px; }
  .label--wash .illustration {
    top: 385px; height: 160px;
    background: radial-gradient(ellipse at 65% 55%, var(--line-teal) 0%, rgba(255,255,255,0) 65%);
  }
  .label--gel .illustration {
    top: 178px; height: 80px;
    background: radial-gradient(ellipse at 60% 55%, var(--line-plum) 0%, rgba(255,255,255,0) 65%);
  }

  .band {
    position: absolute; left: 0; right: 0;
    color: #fff; line-height: 1.15; border-bottom: 4px solid var(--gold);
    display: flex; flex-direction: column; justify-content: center;
  }
  .label--wash .band { top: 550px; height: 62px; background: var(--teal-band); font-size: 20px; }
  .label--gel .band  { top: 262px; height: 48px; background: var(--plum-band); font-size: 15px; }

  .scent {
    position: absolute; top: 646px; left: 50%; transform: translateX(-50%);
    border: 1.5px solid var(--teal); color: var(--teal);
    font-size: 20px; padding: 2px 10px; white-space: nowrap;
  }

  .volume { position: absolute; left: 0; right: 0; }
  .label--wash .volume { top: 736px; font-size: 21px; }
  .label--gel .volume  { top: 344px; font-size: 15px; }
</style>
</head>
<body>

  <section class="label label--wash">
    <div class="brand">Ma Vitrine</div>
    <h1 class="product">Hand &amp;<br>Body Wash</h1>
    <p class="claim">Moisturizing<br>Loremp ipsum dolor sit</p>
    <div class="illustration" role="img" aria-label="Line-drawn flower and leaf illustration in pale teal"></div>
    <p class="band">Lorem ipsum dolor sit amet<br>videntur parum clari</p>
    <p class="scent">vanilla coconut</p>
    <p class="volume">12 fl oz (350ml)</p>
  </section>

  <section class="label label--gel">
    <div class="brand">Ma Vitrine</div>
    <h2 class="product">Shower Gel</h2>
    <p class="claim">Nourishing<br>Loremp ipsum dolor sit</p>
    <div class="illustration" role="img" aria-label="Line-drawn flower and leaf illustration in pale plum"></div>
    <p class="band">Lorem ipsum dolor sit amet<br>videntur parum clari</p>
    <p class="volume">12 fl oz (350ml)</p>
  </section>

</body>
</html>
```